Project, Programme and Portfolio Management Consultant needs a business card

I have recently had someone create a brand guide for me and I wish to have new business cards that incorporate the new brand. I am an independent management consultant working with businesses to improve their ability to deliver their business strategy through selecting the right project, the right people and doing it in the right way. Whilst I am currently working on my own, I am hoping to start to build win business where I need to bring in a team and this branding activity is the start of that process.

Target Market(s)

Medium to large businesses, government departments and defence

Contact Information for Business Card

Name
job title
business name
mobile
email
website
linkedIn profile

Font styles to use
Other font styles liked:
• roboto light

Colors

Designer to choose colors to be used in the design.

Requirements
Must have
• Must use my logo and brand colours (see attached brand guide)

```html
<!DOCTYPE html>
<html lang="en">
<head>
<meta charset="utf-8">
<title>Trilane Consultant – Business Card</title>
<link rel="stylesheet" href="https://fonts.googleapis.com/css2?family=Lato:wght@400;700&family=Mulish:wght@800&display=swap">
<style>
  :root {
    --navy: #10345e;
    --navy-deep: #0d2c52;
    --gold: #d7a21e;
    --paper: #ffffff;
    --paper-shade: #ececec;
    --stage: #e7e5e2;
    --white: #ffffff;
  }
  * { box-sizing: border-box; margin: 0; padding: 0; }
  html, body {
    width: 1200px; height: 900px; overflow: hidden;
    background: var(--stage);
    font-family: "Lato", Arial, sans-serif;
  }
  .canvas { position: relative; width: 1200px; height: 900px; }

  .card {
    position: absolute;
    width: 700px; height: 400px;
    border-bottom: 5px solid var(--gold);
    border-left: 3px solid var(--gold);
    box-shadow: 0 10px 24px rgba(0,0,0,0.18);
  }

  /* Front */
  .card-front {
    left: 70px; top: 40px;
    background: linear-gradient(180deg, var(--paper-shade) 0%, var(--paper) 100%);
    color: var(--navy);
  }
  .holder { position: absolute; left: 60px; top: 88px; }
  .holder-name {
    font-family: "Mulish", Arial, sans-serif;
    font-weight: 800; font-size: 38px; line-height: 1; color: var(--navy);
  }
  .holder-title { font-size: 19px; color: var(--gold); margin-top: 2px; }

  .contact { position: absolute; left: 60px; top: 214px; font-size: 19px; line-height: 1.22; }
  .company { color: var(--navy); letter-spacing: 0.5px; }
  .address { color: var(--gold); }
  .contact-list { list-style: none; margin-top: 6px; }
  .contact-list li { display: flex; align-items: center; gap: 14px; color: var(--gold); height: 27px; }
  .contact-icon { width: 20px; height: 20px; flex: none; }

  .brand-front {
    position: absolute; right: 80px; top: 150px;
    display: flex; align-items: center; gap: 14px;
    font-size: 48px; font-weight: 400; letter-spacing: 6px; color: var(--navy);
  }
  .brand-dot { width: 22px; height: 22px; border-radius: 50%; background: var(--gold); }

  /* Back */
  .card-back {
    left: 430px; top: 478px;
    background: linear-gradient(135deg, var(--navy) 0%, var(--navy-deep) 100%);
    display: flex; align-items: center; justify-content: center;
  }
  .brand-back {
    display: flex; align-items: center; gap: 16px;
    font-size: 56px; font-weight: 400; letter-spacing: 7px; color: var(--white);
  }
  .brand-back .brand-dot { width: 26px; height: 26px; }
</style>
</head>
<body>
<main class="canvas">

  <section class="card card-front" aria-label="Business card front">
    <div class="holder">
      <h1 class="holder-name">Elliot Varne</h1>
      <p class="holder-title">Founder &amp; CEO</p>
    </div>

    <div class="contact">
      <p class="company">TRILANE CONSULTANT LLC</p>
      <p class="address">48 Harbor Lane,<br>2nd FL Fairview, NY 10099</p>
      <ul class="contact-list">
        <li>
          <svg class="contact-icon" viewBox="0 0 20 20" aria-hidden="true">
            <path d="M5 2 L8 6 L6.5 8 Q8 11.5 12 13.5 L14 12 L18 15 L16 18 Q9 18 5 13 Q2 9 5 2 Z" fill="var(--navy)"/>
          </svg>
          <span>1234567890</span>
        </li>
        <li>
          <svg class="contact-icon" viewBox="0 0 20 20" aria-hidden="true">
            <rect x="1.5" y="4" width="17" height="12" fill="var(--navy)"/>
            <path d="M1.5 4 L10 11 L18.5 4" fill="none" stroke="var(--white)" stroke-width="1.4"/>
          </svg>
          <span>info@yourmail.com</span>
        </li>
        <li>
          <svg class="contact-icon" viewBox="0 0 20 20" aria-hidden="true">
            <g fill="none" stroke="var(--navy)" stroke-width="1.4">
              <circle cx="10" cy="10" r="8"/>
              <ellipse cx="10" cy="10" rx="3.5" ry="8"/>
              <path d="M2 10 H18 M3.5 6 H16.5 M3.5 14 H16.5"/>
            </g>
          </svg>
          <span>www.yourwebsite.com</span>
        </li>
        <li>
          <svg class="contact-icon" viewBox="0 0 20 20" aria-hidden="true">
            <circle cx="10" cy="10" r="8" fill="none" stroke="var(--navy)" stroke-width="1.6"/>
          </svg>
          <span>profile.yourwebsite.com</span>
        </li>
      </ul>
    </div>

    <div class="brand-front">
      <span class="brand-dot" aria-hidden="true"></span>
      <span class="brand-name">TRILANE</span>
    </div>
  </section>

  <section class="card card-back" aria-label="Business card back">
    <div class="brand-back">
      <span class="brand-dot" aria-hidden="true"></span>
      <span class="brand-name">TRILANE</span>
    </div>
  </section>

</main>
</body>
</html>
```